Business cards for start-up accounting firm

I'm looking for a double sided business card ready for upload into Lumo print or similar print providers with no modification required by me.
I'm looking for something simple as i think cards that are too 'busy' actually detract from the message. I have some thoughts but more than happy to see what comes up. The logo i have came out of left field and i love it the moment i saw it!

My thoughts:

Side 1: Just the logo, perhaps on a dark grey or charcoal background to make the logo colours stand out?

Side 2: The call to action from me website 'Looking for a more relaxed, friendly and interactive relationship with your accountant?' with my contact information
Name: Gus Tarrow
Email: gus@ledgerowl.com.au
Website: www.ledgerowl.com.au
Phone: 1300 762 349

The call to action needs to be the first thing they see when they look at side 2. If it helps to know what we do and how we do it there is a draft website at www.ledgerowl.com.au

Like i said, happy to consider anything that comes up :)

Target Market(s)

i'm targeting small business owners who experience a lot of stress around finacial reporting and have had bad experiences with accountants in the past.

Industry/Entity Type

Accounting

Contact Information for Business Card

Contained in the Description

Font styles to use
Serif
Sans Serif
Other font styles liked:
• See logo files attached

Colors
474747

Requirements
Must have
• My logo, slogan and contact information

```html
<!DOCTYPE html>
<html lang="en">
<head>
<meta charset="utf-8">
<title>Ledger Owl – Business Cards</title>
<link rel="stylesheet" href="https://fonts.googleapis.com/css2?family=Roboto:wght@400;500;900&display=swap">
<style>
  :root {
    --backdrop: #e9e4dc;
    --card-white: #ffffff;
    --brand-purple: #8c2b84;
    --brand-yellow: #f5c814;
    --ink-grey: #474747;
    --soft-white: #f3e6f1;
    --line-light: rgba(255,255,255,0.55);
  }
  * { box-sizing: border-box; margin: 0; padding: 0; }
  html, body {
    width: 1200px; height: 950px; overflow: hidden;
    background: var(--backdrop);
    font-family: "Roboto", Arial, sans-serif;
  }
  .canvas {
    width: 1200px; height: 950px;
    display: flex; flex-direction: column;
    align-items: center; justify-content: center; gap: 48px;
  }
  .card {
    width: 720px; height: 412px;
    border-radius: 4px;
    box-shadow: 0 6px 18px rgba(0,0,0,0.18);
    display: flex; flex-direction: column; align-items: center;
  }
  .card--front { background: var(--card-white); padding-top: 96px; }
  .card--back { background: var(--brand-purple); padding-top: 80px; }

  .brand { display: flex; align-items: center; gap: 14px; }
  .brand__dot {
    width: 34px; height: 34px; border-radius: 50%;
    background: var(--brand-yellow);
  }
  .brand__name {
    font-weight: 900; font-size: 62px; letter-spacing: 1px;
    text-transform: uppercase; line-height: 1;
  }
  .card--front .brand__name { color: var(--brand-purple); }
  .card--back .brand__name { color: var(--card-white); }

  .slogan {
    margin-top: 16px;
    font-weight: 400; font-size: 17px; letter-spacing: 1px;
  }
  .card--front .slogan { color: var(--ink-grey); }
  .card--back .slogan { color: var(--soft-white); }

  .call-to-action {
    margin-top: 48px; max-width: 470px;
    text-align: center; color: var(--ink-grey);
    font-size: 21px; line-height: 1.4; font-weight: 400;
  }

  .holder {
    display: flex; align-items: center; gap: 16px;
    margin-top: 40px;
    color: var(--brand-yellow); font-weight: 500; font-size: 28px;
  }
  .holder::before, .holder::after {
    content: ""; width: 130px; height: 1px; background: var(--line-light);
  }

  .contacts {
    display: flex; gap: 40px; margin-top: 22px;
    color: var(--card-white); font-size: 18px;
  }
  .contacts__col { display: flex; flex-direction: column; gap: 12px; justify-content: flex-end; }
  .contact { display: flex; align-items: center; gap: 9px; }
  .contact svg { width: 18px; height: 18px; flex: none; }
</style>
</head>
<body>
<main class="canvas">

  <section class="card card--front" aria-label="Business card front">
    <div class="brand">
      <span class="brand__dot"></span>
      <span class="brand__name">Ledger Owl</span>
    </div>
    <p class="slogan">Calm books. Clear minds.</p>
    <p class="call-to-action">Looking for a more relaxed, friendly and interactive relationship with your accountant?</p>
  </section>

  <section class="card card--back" aria-label="Business card back">
    <div class="brand">
      <span class="brand__dot"></span>
      <span class="brand__name">Ledger Owl</span>
    </div>
    <p class="slogan">Calm books. Clear minds.</p>
    <p class="holder">Gus Tarrow</p>
    <div class="contacts">
      <div class="contacts__col">
        <p class="contact">
          <svg viewBox="0 0 24 24" aria-hidden="true"><path fill="#f5c814" d="M6.6 10.8a15.1 15.1 0 0 0 6.6 6.6l2.2-2.2a1 1 0 0 1 1-.25 11.4 11.4 0 0 0 3.6.57 1 1 0 0 1 1 1V20a1 1 0 0 1-1 1A17 17 0 0 1 3 4a1 1 0 0 1 1-1h3.5a1 1 0 0 1 1 1c0 1.25.2 2.45.57 3.57a1 1 0 0 1-.25 1z"/></svg>
          1300 762 349
        </p>
      </div>
      <div class="contacts__col">
        <p class="contact">
          <svg viewBox="0 0 24 24" aria-hidden="true"><rect x="2" y="5" width="20" height="14" rx="1.5" fill="#f5c814"/><path d="M3 6.5l9 6.5 9-6.5" fill="none" stroke="#8c2b84" stroke-width="1.8"/></svg>
          gus@ledgerowl.com.au
        </p>
        <p class="contact">
          <svg viewBox="0 0 24 24" aria-hidden="true"><circle cx="12" cy="12" r="10" fill="#f5c814"/><path d="M2 12h20M12 2c3 3 3 17 0 20M12 2c-3 3-3 17 0 20" fill="none" stroke="#8c2b84" stroke-width="1.5"/></svg>
          ledgerowl.com.au
        </p>
      </div>
    </div>
  </section>

</main>
</body>
</html>
```